M Zyvantics Buisness Cards

I need a technology focused clean business card for my employees. I have attached out logo to include in the mocks. We're a modern tech consulting firm that drives to interface humanity with technology in a truly cohesive fashion.

```html
<!DOCTYPE html>
<html lang="en">
<head>
<meta charset="utf-8">
<title>M Zyvantics Business Cards</title>
<link href="https://fonts.googleapis.com/css2?family=Montserrat:wght@400;500;700&display=swap" rel="stylesheet">
<style>
  :root {
    --brand-blue: #2474b0;
    --ink-grey: #55585c;
    --rule-grey: #c9ccd0;
    --card-white: #ffffff;
    --backdrop: #ecedef;
    --net-light: #5d9bcc;
  }
  * { margin: 0; padding: 0; box-sizing: border-box; }
  html, body { width: 1200px; height: 1138px; overflow: hidden; }
  body {
    background: var(--backdrop);
    font-family: "Montserrat", sans-serif;
    display: flex;
    flex-direction: column;
    align-items: center;
    justify-content: center;
    gap: 60px;
  }
  .card {
    width: 880px;
    height: 503px;
    position: relative;
    box-shadow: 0 6px 18px rgba(0,0,0,0.12);
  }
  /* Front */
  .card-front { background: var(--card-white); display: flex; align-items: center; }
  .front-brand {
    width: 440px;
    display: flex;
    align-items: center;
    justify-content: center;
    gap: 16px;
  }
  .brand-dot {
    width: 30px; height: 30px; border-radius: 50%;
    background: var(--brand-blue);
  }
  .brand-name {
    font-weight: 700;
    font-size: 44px;
    color: var(--ink-grey);
    letter-spacing: 1px;
  }
  .divider {
    width: 1px; height: 220px; background: var(--rule-grey);
  }
  .front-details { padding-left: 44px; color: var(--ink-grey); }
  .person-name {
    font-weight: 700; font-size: 24px; letter-spacing: 1px;
    text-transform: uppercase; color: #3f4246;
  }
  .person-role { font-size: 19px; color: var(--brand-blue); margin-bottom: 14px; }
  .address { font-size: 18px; line-height: 1.35; margin-bottom: 8px; }
  .contact-list { list-style: none; font-size: 18px; line-height: 1.45; }
  .contact-list li { display: flex; align-items: center; gap: 12px; }
  .contact-list svg { width: 16px; height: 16px; flex: none; }
  /* Back */
  .card-back { background: var(--brand-blue); overflow: hidden; }
  .network-area {
    position: absolute; left: 0; top: 0; width: 420px; height: 100%;
    background: linear-gradient(110deg, rgba(255,255,255,0.18), rgba(255,255,255,0) 85%);
  }
  .back-brand {
    position: absolute; left: 470px; top: 190px;
    display: flex; align-items: center; gap: 16px;
  }
  .back-brand .brand-dot { background: var(--card-white); }
  .back-brand .brand-name { color: var(--card-white); font-size: 50px; }
  .back-web {
    position: absolute; right: 70px; bottom: 50px;
    color: var(--card-white); font-weight: 500; font-size: 19px; letter-spacing: 1px;
  }
</style>
</head>
<body>
  <section class="card card-front">
    <div class="front-brand">
      <span class="brand-dot"></span>
      <span class="brand-name">M Zyvantics</span>
    </div>
    <div class="divider"></div>
    <div class="front-details">
      <p class="person-name">Dorian Vale</p>
      <p class="person-role">Managing Director</p>
      <p class="address">Kelmstraat 48<br>4100 Arvenhal</p>
      <ul class="contact-list">
        <li><svg viewBox="0 0 16 16"><path d="M4 1 L6.5 4.5 L5 6 Q6.5 9.5 10 11 L11.5 9.5 L15 12 L13 15 Q3 13 1 3 Z" fill="#2474b0"/></svg>+ 32 555 0148 27</li>
        <li><svg viewBox="0 0 16 16"><rect x="1" y="3" width="14" height="10" fill="none" stroke="#2474b0" stroke-width="1.4"/><path d="M1 3 L8 9 L15 3" fill="none" stroke="#2474b0" stroke-width="1.4"/></svg>dorian@zyvantics.example</li>
        <li><svg viewBox="0 0 16 16"><circle cx="8" cy="8" r="6.5" fill="none" stroke="#2474b0" stroke-width="1.4"/><ellipse cx="8" cy="8" rx="3" ry="6.5" fill="none" stroke="#2474b0" stroke-width="1.2"/><path d="M1.5 8 H14.5" stroke="#2474b0" stroke-width="1.2"/></svg>www.zyvantics.example</li>
      </ul>
    </div>
  </section>

  <section class="card card-back">
    <div class="network-area" role="img" aria-label="Decorative network pattern of connected dots and lines"></div>
    <div class="back-brand">
      <span class="brand-dot"></span>
      <span class="brand-name">M Zyvantics</span>
    </div>
    <p class="back-web">www.zyvantics.example</p>
  </section>
</body>
</html>
```